Savour and Thrive Wellbeing is being Launched and needs a business card and stationery package

I need a stationery package including business card (primary focus) , letterhead, digital letterhead, envelopes, with compliments slip, A 5 note sheet for the rebranding of my business and launch of my new website. I have a logo, like beige, brown earthy tones with a hint of red. I would also like the option of my letterhead also being printed on recycled paper in another format as well as the traditional letterhead. I do also send my letters to GPs and specialists digitally as well. I like to stand out from the usual stereotype of fruits and vegetables on business cards as I find that quite tacky and stereotypical. I want the business card to capture the essence of my logo as natural, nutrition, enjoyment, nurturing and freedom with food. I have attached the logo, and additional brief sheet on my ideas. Happy to have any background that is complementary to my theme, and what you believe would be catching. Definitely DONT'T like pink, try to pick up the darker colour in the logo please. and think too much black is a little overpowering.

Target Market(s)

clients who are interested in improving their health and wellness. Client 80% females; 20% males

Industry/Entity Type

Health And Wellness

Contact Information for Business Card

I am open to having different backgrounds as well that would complement the logo. Probably less emphasis on the heart out of the logo - just happy to keep that in the logo only please
I am also wanting two business cards - one for the appointments, one for general distribution and media distribution (both need to look consistent though) - but does give opportunity for one of the business cards to be less wordy and more striking. And the front of the business card can certainly stand out with the entire savour and thrive logo and my name and grab the attention of the receiver.
1st business card
on front:
Lorena Whitcombe
Savour and Thrive Wellbeing & logo
Nutritionist and Dietitian
Tarvel Medical Centre
647 Brindle Hill Rd, Quorrel Q 4987
Phone: (07) 3017 2968 Fax: (07) 3156 7209
Mobile: 0400 261 937
www.savourandthrivewellbeing.example.au
lorena@savourandthrivewellbeing.example.au
on back:
next appointment

……………………….. at ……………………… (possibly 4 times)
If you are unable to keep your appointment, please contact us as soon as possible (small font)
2nd business card (needs to be very eye catching and stand out)
on front: Savour and Thrive Wellbeing logo and my name
on back:
Lorena Whitcombe
address
phones, fax, website, email address

Font styles to use
Other font styles liked:
• please refer to logo

Requirements
Must have
• refreshing and simple; new and vibrant - I am rebranding my business after 20 years
• to get a feel of what is the theme - go to my new website (not completed as yet - but you will get a preliminary view) - don't do as google search as blocked - but can put into website header and it will be shown
• www.savourandthrivewellbeing.example.au - but please ignore the colouring of the 4 blocks under the slider on the home page - I am not wanting these colourings - they are getting updated.
Nice to have
• earthy tones, beige, hint of red, fonts to match logo if possible, organic, modern
• get inspiration from my logo please, open to having other backgrounds that complement
Should not have
• no food shots or stereotypical weight/ scales images
• no green, yellow or orange

```html
<!DOCTYPE html>
<html lang="en">
<head>
<meta charset="utf-8">
<title>Savour and Thrive Wellbeing – Business Cards</title>
<link rel="stylesheet" href="https://fonts.googleapis.com/css2?family=Open+Sans:wght@400;600;700&display=swap">
<style>
  :root {
    --backdrop: #cfc3b3;
    --card-brown: #4a3226;
    --card-beige: #f3ebdd;
    --brand-red: #9e3b2f;
    --brand-sand: #e3cba8;
    --icon-red: #d0705c;
    --text-cream: #f6eee2;
    --text-brown: #3b2a20;
    --dots-brown: #8a7362;
    --divider: #614436;
  }
  * { box-sizing: border-box; margin: 0; padding: 0; }
  html, body { width: 1200px; height: 900px; overflow: hidden; }
  body {
    background: var(--backdrop);
    font-family: "Open Sans", Arial, sans-serif;
    position: relative;
  }
  .card {
    position: absolute;
    top: 290px;
    width: 520px;
    height: 320px;
    border-radius: 22px;
    overflow: hidden;
    box-shadow: 0 12px 30px rgba(60, 40, 25, 0.35);
  }

  /* Contact card */
  .card--contact {
    left: 60px;
    background: var(--card-brown);
    color: var(--text-cream);
  }
  .contact-brand {
    position: absolute;
    left: 0; top: 0;
    width: 200px; height: 100%;
    display: flex; flex-direction: column;
    align-items: center; justify-content: center;
    gap: 14px;
    border-right: 1px solid var(--divider);
    padding: 0 18px;
  }
  .brand-dot {
    width: 54px; height: 54px;
    border-radius: 50%;
    background: var(--brand-red);
  }
  .card--contact .brand-name {
    color: var(--brand-sand);
  }
  .brand-name {
    font-weight: 600;
    font-size: 18px;
    line-height: 1.3;
    text-align: center;
  }
  .contact-details {
    position: absolute;
    left: 218px; top: 38px;
    right: 14px;
    font-size: 12.5px;
    line-height: 1.35;
  }
  .person-name { font-weight: 700; font-size: 16px; }
  .person-role { font-size: 14px; margin-bottom: 20px; }
  .address { margin-bottom: 14px; font-size: 13px; }
  .contact-group { list-style: none; margin-bottom: 12px; }
  .contact-group li {
    display: flex; align-items: center; gap: 8px;
    white-space: nowrap;
  }
  .contact-group svg { width: 10px; height: 10px; flex: none; fill: var(--icon-red); }

  /* Appointment card */
  .card--appointment {
    left: 620px;
    background: var(--card-beige);
    color: var(--text-brown);
  }
  .appointment-brand {
    margin-top: 44px;
    display: flex; align-items: center; justify-content: center; gap: 10px;
  }
  .appointment-brand .brand-dot { width: 16px; height: 16px; }
  .appointment-brand .brand-name {
    color: var(--text-brown);
    font-size: 20px;
  }
  .appointment-title {
    font-weight: 700;
    font-size: 14px;
    margin: 40px 0 6px 40px;
  }
  .appointment-lines { list-style: none; margin-left: 40px; }
  .appointment-lines li {
    display: flex; align-items: flex-end; gap: 6px;
    width: 430px; height: 22px;
    font-weight: 700; font-size: 13px;
  }
  .appointment-lines .dots {
    flex: 1;
    border-bottom: 2px dotted var(--dots-brown);
    height: 14px;
  }
  .appointment-note {
    font-size: 10px;
    color: var(--text-brown);
    text-align: center;
    margin-top: 18px;
  }
</style>
</head>
<body>

<section class="card card--contact">
  <div class="contact-brand">
    <span class="brand-dot"></span>
    <span class="brand-name">Savour and Thrive Wellbeing</span>
  </div>
  <div class="contact-details">
    <p class="person-name">Lorena Whitcombe</p>
    <p class="person-role">Nutritionist and Dietitian</p>
    <p class="address">Tarvel Medical Centre<br>647 Brindle Hill Rd, Quorrel Q 4987</p>
    <ul class="contact-group">
      <li><svg viewBox="0 0 10 10"><path d="M1 3c0-1 1-2 4-2s4 1 4 2v1H7V3H3v1H1zM2 5h6l1 4H1z"/></svg>(07) 3017 2968</li>
      <li><svg viewBox="0 0 10 10"><path d="M3 0h4v3H3zM1 3h8v5H7v2H3V8H1zM4 7v2h2V7z"/></svg>(07) 3156 7209</li>
    </ul>
    <ul class="contact-group">
      <li><svg viewBox="0 0 10 10"><path d="M2.5 0h5v10h-5zM3.5 1v7h3V1z"/></svg>0400 261 937</li>
      <li><svg viewBox="0 0 10 10"><path d="M0 2h10v6H0zM1 3l4 3 4-3z"/></svg>lorena@savourandthrivewellbeing.example.au</li>
      <li><svg viewBox="0 0 10 10"><circle cx="5" cy="5" r="5"/></svg>www.savourandthrivewellbeing.example.au</li>
    </ul>
  </div>
</section>

<section class="card card--appointment">
  <div class="appointment-brand">
    <span class="brand-dot"></span>
    <span class="brand-name">Savour and Thrive Wellbeing</span>
  </div>
  <p class="appointment-title">Next Appointment</p>
  <ul class="appointment-lines">
    <li><span class="dots"></span>at<span class="dots"></span></li>
    <li><span class="dots"></span>at<span class="dots"></span></li>
    <li><span class="dots"></span>at<span class="dots"></span></li>
    <li><span class="dots"></span>at<span class="dots"></span></li>
  </ul>
  <p class="appointment-note">If you are unable to keep your appointment, please contact us as soon as possible</p>
</section>

</body>
</html>
```